Business Card Design Project

I need some business cards with the logo you did for us (attached)
I am looking for a coulourful yet serious business card

We do market research
on the back I want the logo

on the front my name : Corinne Valdessac
position : Manager
address : Brume Analytica Sarl - 27 Rue des tanneurs
1847 Glarency - Switzerland
corinne.valdessac@brumeanalytica.ch
Tel : +4122 934 07 58
Mob France :+33 671 42 8356
Mob Italy +39 347 520 8163

The tree of the logo could also be used alone

THE BACKGROUND COLOR ON THE FRONT HAS TO BE WHITE, ON THE BACK YU CAN TRY OHER COLOUR BUT HOMOGENEOUS (NOT EXPENSIVE TO PRINT)

Target Market(s)

multinational companies or other market research companies

Industry/Entity Type

Market Research

Requirements
Must have
• logo on the back
and all the info above

```html
<!DOCTYPE html>
<html lang="en">
<head>
<meta charset="utf-8">
<title>Brume Analytica business card</title>
<link rel="stylesheet" href="https://fonts.googleapis.com/css2?family=Libre+Baskerville:ital,wght@0,400;1,400&display=swap">
<style>
  :root {
    --stage: #3b2a20;
    --card-white: #ffffff;
    --card-dark-center: #5b524c;
    --card-dark-edge: #352e2a;
    --ink: #1c1a19;
    --accent: #c8203f;
    --rule: #8a8583;
    --brand-soft: #e9e2da;
  }
  * { margin: 0; padding: 0; box-sizing: border-box; }
  html, body {
    width: 848px;
    height: 1200px;
    overflow: hidden;
    background: var(--stage);
  }
  body {
    position: relative;
    font-family: "Libre Baskerville", "Baskerville", Georgia, serif;
    color: var(--ink);
  }
  .card {
    position: absolute;
    width: 222px;
    height: 342px;
  }
  .card-back {
    left: 162px;
    top: 328px;
    background: radial-gradient(ellipse at 50% 45%, var(--card-dark-center) 0%, var(--card-dark-edge) 85%);
    display: flex;
    align-items: center;
    justify-content: center;
  }
  .card-back .brand {
    display: flex;
    align-items: center;
    gap: 8px;
    color: var(--brand-soft);
    font-size: 15px;
  }
  .brand-dot {
    width: 10px;
    height: 10px;
    border-radius: 50%;
    background: currentColor;
  }
  .card-front {
    left: 465px;
    top: 326px;
    background: var(--card-white);
    padding: 0 18px 0 24px;
  }
  .card-front .brand {
    position: absolute;
    left: 24px;
    top: 64px;
    display: flex;
    align-items: center;
    gap: 7px;
    color: var(--accent);
    font-size: 14px;
  }
  .holder {
    position: absolute;
    left: 24px;
    top: 132px;
  }
  .holder-name {
    font-size: 16px;
    line-height: 1.1;
    font-weight: 400;
  }
  .holder-name em { font-style: italic; }
  .holder-role {
    color: var(--accent);
    font-size: 11px;
    margin-top: 3px;
  }
  .contact {
    position: absolute;
    left: 24px;
    right: 18px;
    top: 192px;
    font-size: 9.6px;
    line-height: 14.5px;
  }
  .contact dt { display: inline; font-style: italic; }
  .contact dd { display: inline; }
  .contact dd::after { content: ""; display: block; }
  .rule {
    position: absolute;
    left: 24px;
    right: 18px;
    top: 245px;
    border-top: 1px dotted var(--rule);
  }
  .address {
    position: absolute;
    left: 24px;
    top: 252px;
    font-size: 9.6px;
    line-height: 13px;
    font-style: normal;
  }
  .email {
    position: absolute;
    left: 24px;
    top: 301px;
    font-size: 7.6px;
    font-style: italic;
  }
</style>
</head>
<body>
  <section class="card card-back" aria-label="Card back">
    <div class="brand"><span class="brand-dot"></span><span>brume analytica</span></div>
  </section>

  <section class="card card-front" aria-label="Card front">
    <div class="brand"><span class="brand-dot"></span><span>brume analytica</span></div>

    <div class="holder">
      <h1 class="holder-name">Corinne<em>Valdessac</em></h1>
      <p class="holder-role">Manager</p>
    </div>

    <dl class="contact">
      <dt>Tel</dt> <dd>: +4122 934 07 58</dd>
      <dt>Mob France</dt> <dd>: +33 671 42 8356</dd>
      <dt>Mob Italy</dt> <dd>: +39 347 520 8163</dd>
    </dl>

    <div class="rule"></div>

    <address class="address">
      Brume Analytica Sarl<br>
      27 Rue Des Tanneurs<br>
      1847 Glarency – Switzerland
    </address>

    <p class="email">corinne.valdessac@brumeanalytica.ch</p>
  </section>
</body>
</html>
```